BrawnCrate placard

I need a placard designed that will go in my monthly subscription boxes to describe the products inside. There must be space to write 3-5 sentences on each product.
the first area will be titled: For your flowing mane
2 for your macho glow
3 to keep you smelling macho
4 to keep you clanging and banging at the gym.
Placard will be 5inchs wide and 7inchs long

I have attached the logo and the website address must be used in the design brawncrates.com.

Target Market(s)

men between 20-50

Colors

Designer to choose colors to be used in the design.

Requirements
Must have
• My website address brawncrates.com
• 4 area to write 3-5 sentences
• 1 for your flowing mane
• 2to keep you smelling macho
• 3 to keep you clanging and banging at the gym
• 4 for your macho glow

```html
<!DOCTYPE html>
<html lang="en">
<head>
<meta charset="utf-8">
<title>BrawnCrate Placard</title>
<link href="https://fonts.googleapis.com/css2?family=Orbitron:wght@700;900&family=Montserrat:wght@400;600&display=swap" rel="stylesheet">
<style>
  :root {
    --stage: #1c2130;
    --card: #121419;
    --card-edge: #0c0d11;
    --red: #e3191b;
    --white: #ffffff;
    --body-text: #e6e6e6;
    --muted: #c9c9c9;
    --photo-dark: #1a1816;
    --photo-light: #cfcfc6;
  }
  * { box-sizing: border-box; margin: 0; padding: 0; }
  html, body {
    width: 1200px; height: 1200px; overflow: hidden;
    background: var(--stage);
  }
  .placard {
    position: absolute; left: 173px; top: 0;
    width: 854px; height: 1200px;
    background: radial-gradient(ellipse at 35% 35%, #1d2026 0%, var(--card) 55%, var(--card-edge) 100%);
    overflow: hidden;
    font-family: 'Montserrat', sans-serif;
  }
  .model-photo {
    position: absolute; left: 455px; top: 0; width: 399px; height: 1200px;
    background:
      linear-gradient(90deg, var(--card) 0%, rgba(18,20,25,0) 30%),
      linear-gradient(180deg, var(--photo-dark) 0%, #6b5446 22%, #3b3029 36%, var(--photo-light) 50%, #bdbdb4 78%, #2a2a2c 90%, var(--photo-dark) 100%);
  }
  .brand {
    position: absolute; left: 40px; width: 300px; top: 222px; text-align: center;
  }
  .brand-name {
    display: flex; align-items: center; justify-content: center; gap: 10px;
    font-family: 'Orbitron', sans-serif; font-weight: 900; font-size: 29px;
    color: var(--white); letter-spacing: 1px;
  }
  .brand-mark { width: 18px; height: 18px; background: var(--red); }
  .brand-tagline {
    margin-top: 6px; font-family: 'Montserrat', sans-serif; font-weight: 600;
    font-size: 7.5px; color: var(--white); letter-spacing: 0.2px; text-transform: uppercase;
  }
  .product-box {
    position: absolute; left: 85px; top: 311px; width: 258px; height: 275px;
    background: linear-gradient(160deg, #f2f2f2 0%, #d9d9d7 45%, #9c9c9a 100%);
    clip-path: polygon(35% 0, 100% 20%, 93% 75%, 55% 100%, 5% 75%, 0 28%);
  }
  .features { position: absolute; left: 30px; top: 612px; width: 420px; }
  .feature { position: absolute; left: 0; display: flex; gap: 18px; }
  .feature-icon {
    flex: none; width: 44px; height: 72px; border-radius: 22px 22px 18px 18px;
    background: var(--white); margin-top: 14px;
  }
  .feature-title {
    font-family: 'Orbitron', sans-serif; font-weight: 700; font-size: 15.5px;
    color: var(--red); line-height: 20px; text-transform: uppercase; letter-spacing: 0.3px;
  }
  .feature-copy {
    margin-top: 4px; font-size: 11.5px; line-height: 14.3px; color: var(--body-text);
  }
  .feature--mane { top: 0; }
  .feature--scent { top: 109px; left: 6px; }
  .feature--gym { top: 225px; }
  .feature--glow { top: 359px; }
  .contact { position: absolute; left: 29px; top: 1110px; }
  .contact-call {
    font-family: 'Orbitron', sans-serif; font-weight: 900; font-size: 27px;
    color: var(--red); letter-spacing: 0.3px; white-space: nowrap;
  }
  .contact-web {
    margin-top: 6px; font-size: 19px; color: var(--white); letter-spacing: 10.5px;
  }
</style>
</head>
<body>
  <main class="placard">
    <div class="model-photo" role="img" aria-label="Photo of a young man with styled hair and a beard wearing a white V-neck t-shirt and dark jeans"></div>

    <header class="brand">
      <div class="brand-name"><span class="brand-mark"></span>BrawnCrate</div>
      <p class="brand-tagline">Mens grooming and essentials for the everyday macho man</p>
    </header>

    <div class="product-box" role="img" aria-label="White square subscription gift box with the brand name on the lid"></div>

    <section class="features">
      <article class="feature feature--mane">
        <div class="feature-icon" role="img" aria-label="Bearded man icon"></div>
        <div>
          <h2 class="feature-title">For your flowing mane</h2>
          <p class="feature-copy">Lorem ipsum dolor sit amet, consectetur adipiscing<br>elit, sed do eiusmod tempor incididunt ut labore et<br>dolore magna aliqua. Ut enim ad minim veniam, quis<br>nostrud exercitation ullamco laboris nisi ut aliquip ex.</p>
        </div>
      </article>
      <article class="feature feature--scent">
        <div class="feature-icon" role="img" aria-label="Bearded man with glasses icon"></div>
        <div>
          <h2 class="feature-title">To keep you smelling macho</h2>
          <p class="feature-copy">Lorem ipsum dolor sit amet, consectetur adipiscing elit,<br>sed do eiusmod tempor incididunt ut labore et dolore<br>magna aliqua. Ut enim ad minim veniam, quis nostrud<br>exercitation ullamco laboris nisi ut aliquip ex.</p>
        </div>
      </article>
      <article class="feature feature--gym">
        <div class="feature-icon" role="img" aria-label="Man with glasses and moustache icon"></div>
        <div>
          <h2 class="feature-title">To keep you clanging and<br>banging at the gym</h2>
          <p class="feature-copy">Lorem ipsum dolor sit amet, consectetur adipiscing<br>elit, sed do eiusmod tempor incididunt ut labore et<br>dolore magna aliqua. Ut enim ad minim veniam, quis<br>nostrud exercitation ullamco laboris nisi ut aliquip ex.</p>
        </div>
      </article>
      <article class="feature feature--glow">
        <div class="feature-icon" role="img" aria-label="Bearded man with sunglasses icon"></div>
        <div>
          <h2 class="feature-title">For your macho glow</h2>
          <p class="feature-copy">Lorem ipsum dolor sit amet, consectetur adipiscing<br>elit, sed do eiusmod tempor incididunt ut labore et<br>dolore magna aliqua. Ut enim ad minim veniam, quis<br>nostrud exercitation ullamco laboris nisi ut aliquip ex.</p>
        </div>
      </article>
    </section>

    <footer class="contact">
      <p class="contact-call">Call BrawnCrate toll free 1-866-555-0142</p>
      <p class="contact-web">www.brawncrates.com</p>
    </footer>
  </main>
</body>
</html>
```